" Algo diferente do que se encontra no que diz respeito ao Personal Trainer. Quero vender Qualidade de Vida, fugindo um pouco dos Halteres dos Cartoes de Visitas de Personais que ja vi! "

```html
<!DOCTYPE html>
<html lang="pt-BR">
<head>
<meta charset="UTF-8">
<title>Caio Ferraz – Personal Trainer</title>
<link rel="stylesheet" href="https://fonts.googleapis.com/css2?family=Saira+Semi+Condensed:wght@500;700&display=swap">
<style>
  :root {
    --backdrop: #141414;
    --card-navy: #0b1621;
    --brand-blue: #2f8fd8;
    --text-light: #f2f4f6;
    --text-muted: #c9d0d6;
  }
  * { box-sizing: border-box; margin: 0; padding: 0; }
  html, body {
    width: 1200px; height: 1200px; overflow: hidden;
    background: var(--backdrop);
    font-family: "Saira Semi Condensed", "Arial Narrow", sans-serif;
  }
  .canvas { position: relative; width: 1200px; height: 1200px; }

  .card {
    position: absolute;
    background: var(--card-navy);
    overflow: hidden;
  }
  .card--front { left: 103px; top: 72px; width: 917px; height: 508px; }
  .card--back  { left: 185px; top: 629px; width: 914px; height: 504px; }

  .wordmark {
    display: flex; align-items: center; gap: 14px;
    font-weight: 700; letter-spacing: 1px; text-transform: uppercase;
    white-space: nowrap;
  }
  .wordmark__dot { border-radius: 50%; flex: none; }

  /* Front */
  .front__mark {
    position: absolute; left: 0; right: 0; top: 160px;
    justify-content: center; color: var(--brand-blue); font-size: 60px;
  }
  .front__mark .wordmark__dot { width: 46px; height: 46px; background: var(--brand-blue); }
  .front__info {
    position: absolute; left: 0; right: 0; top: 327px;
    text-align: center; line-height: 1;
  }
  .name { font-weight: 700; text-transform: uppercase; letter-spacing: 1px; }
  .role { font-weight: 500; text-transform: uppercase; letter-spacing: 1.5px; }
  .cref { font-weight: 500; text-transform: uppercase; letter-spacing: 1px; color: var(--brand-blue); }
  .front__info .name { font-size: 42px; color: var(--text-light); }
  .front__info .role { font-size: 25px; color: var(--text-light); margin-top: 12px; }
  .front__info .cref { font-size: 20px; margin-top: 10px; }

  /* Back */
  .back__panel { position: absolute; left: 0; top: 0; width: 500px; height: 504px; }
  .back__mark {
    position: absolute; left: 0; width: 458px; top: 235px;
    justify-content: center; color: var(--card-navy); font-size: 50px;
  }
  .back__mark .wordmark__dot { width: 40px; height: 40px; background: var(--card-navy); }
  .back__info {
    position: absolute; right: 56px; top: 68px; text-align: right; line-height: 1;
  }
  .back__info .name { font-size: 36px; color: var(--brand-blue); }
  .back__info .role { font-size: 18px; color: var(--text-muted); margin-top: 10px; }
  .back__info .cref { font-size: 17px; margin-top: 6px; }

  .contacts {
    position: absolute; right: 56px; top: 360px;
    display: flex; flex-direction: column; align-items: flex-end; gap: 14px;
  }
  .contact {
    display: flex; align-items: center; gap: 16px;
    color: var(--text-light); font-size: 25px; font-weight: 500; letter-spacing: 1px;
  }
  .contact__icon { width: 28px; height: 28px; flex: none; }
</style>
</head>
<body>
<main class="canvas">

  <section class="card card--front">
    <div class="wordmark front__mark"><span class="wordmark__dot"></span>Caio Ferraz</div>
    <div class="front__info">
      <p class="name">Caio Ferraz</p>
      <p class="role">Personal Trainer</p>
      <p class="cref">CREF 002731-G/SP</p>
    </div>
  </section>

  <section class="card card--back">
    <svg class="back__panel" viewBox="0 0 500 504" aria-hidden="true">
      <polygon points="0,0 458,0 458,55 499,98 458,140 458,504 0,504" fill="var(--brand-blue)"/>
    </svg>
    <div class="wordmark back__mark"><span class="wordmark__dot"></span>Caio Ferraz</div>

    <div class="back__info">
      <p class="name">Caio Ferraz</p>
      <p class="role">Personal Trainer</p>
      <p class="cref">CREF 002731-G/SP</p>
    </div>

    <div class="contacts">
      <p class="contact">98 4120-5573
        <svg class="contact__icon" viewBox="0 0 28 28" aria-label="Telefone">
          <circle cx="14" cy="14" r="14" fill="var(--brand-blue)"/>
          <path d="M9.5 7.5c.6-.5 1.4-.4 1.8.2l1.4 2.1c.3.5.2 1.2-.2 1.6l-.9.8c.7 1.6 1.9 2.9 3.5 3.7l.8-.9c.4-.4 1.1-.5 1.6-.2l2.1 1.4c.6.4.7 1.2.2 1.8l-1 1.1c-.7.8-1.9 1-2.9.6-3.5-1.4-6.2-4.1-7.6-7.6-.4-1-.2-2.2.6-2.9z" fill="var(--card-navy)"/>
        </svg>
      </p>
      <p class="contact">caiofz@mailbox.com
        <svg class="contact__icon" viewBox="0 0 28 28" aria-label="E-mail">
          <circle cx="14" cy="14" r="14" fill="var(--brand-blue)"/>
          <rect x="7.5" y="9.5" width="13" height="9" rx="1" fill="var(--card-navy)"/>
          <path d="M8 10.2l6 4.6 6-4.6" fill="none" stroke="var(--brand-blue)" stroke-width="1.4"/>
        </svg>
      </p>
    </div>
  </section>

</main>
</body>
</html>
```